Velmora Water Purification

We need a website set up on a "Free account" WordPress platform. (This is the type of Wordpress site that you can sign up for and create online for free (not a server-hosted type.)
The website will be for a water purification company. They install devices in homes to purify the water for safer drinking, bathing, and cleaning.
Our logo is attached. Please keep color scheme of the website consistent with the logo.
Water Purification

```html
<!DOCTYPE html>
<html lang="en">
<head>
<meta charset="utf-8">
<title>Velmora Water Purification</title>
<link href="https://fonts.googleapis.com/css2?family=Oswald:wght@400&family=PT+Sans:wght@400;700&display=swap" rel="stylesheet">
<style>
:root{
  --blue:#1565c0;
  --blue-btn:#1a66d6;
  --blue-band:#1b6fc6;
  --sky-top:#4cc4f2;
  --sky-bot:#1e8fe0;
  --hero-a:#0f5f8c;
  --hero-b:#2aa6d6;
  --ink:#1d1d1d;
  --text:#3a3a3a;
  --muted:#6b6b6b;
  --foot:#f4f4f4;
  --white:#ffffff;
}
*{margin:0;padding:0;box-sizing:border-box}
html,body{width:1200px;height:2812px;overflow:hidden;background:var(--white)}
body{position:relative;font-family:"PT Sans",sans-serif;color:var(--text)}
.abs{position:absolute}

/* header */
.topbar{left:0;top:0;width:1200px;height:60px;background:linear-gradient(180deg,var(--sky-top),var(--sky-bot))}
.nav{left:403px;top:0;height:60px;display:flex}
.nav a{display:block;height:60px;line-height:60px;color:var(--white);text-decoration:none;font-size:18px;text-align:center;border-left:1px solid rgba(255,255,255,.35)}
.nav a.active{background:var(--blue-btn)}
.brand{left:47px;top:0;width:221px;height:135px;background:var(--white);border-radius:0 0 110px 110px;display:flex;align-items:center;justify-content:center;gap:8px;z-index:2}
.brand-dot{width:16px;height:16px;border-radius:50%;background:var(--blue)}
.brand-name{font-size:26px;font-weight:700;color:var(--blue)}

.hero{left:0;top:60px;width:1200px;height:589px;background:radial-gradient(circle at 45% 40%,var(--hero-b),var(--hero-a) 85%)}
.hero-person{left:38px;top:80px;width:392px;height:509px;background:linear-gradient(180deg,#6fb7d3,#3f86a8);border-radius:180px 180px 0 0}
.hero-product{left:460px;top:90px;width:290px;height:520px;background:linear-gradient(180deg,#f2f6fa,#cfe0ee);border-radius:40px 40px 10px 10px}
.hero-title{left:748px;top:195px;width:430px;font-family:"Oswald",sans-serif;font-size:43px;line-height:51px;color:var(--white);text-transform:uppercase}
.btn{display:block;background:var(--blue-btn);color:var(--white);text-align:center;text-decoration:none;text-transform:uppercase}
.hero-btn{left:750px;top:416px;width:118px;height:53px;line-height:53px;font-family:"Oswald",sans-serif;font-size:18px}

/* section titles */
.section-title{left:0;width:1200px;text-align:center;font-size:28px;font-weight:700;color:var(--ink);text-transform:uppercase;letter-spacing:.5px}
.ornament{left:530px;width:140px;height:20px}

/* category cards */
.cat{top:772px;height:362px;background:linear-gradient(180deg,#eef2f5,#dbe2e8)}
.cat h3{position:absolute;left:28px;top:36px;font-size:21px;color:var(--ink)}
.cat p{position:absolute;left:28px;top:70px;width:300px;font-size:15px;line-height:22px;color:var(--ink)}
.cat .shot{position:absolute;right:28px;bottom:30px;width:180px;height:200px;background:linear-gradient(180deg,#5aa0e0,#1c5fb8);border-radius:14px}

/* welcome */
.welcome-text{left:47px;top:1244px;width:1106px;text-align:center;font-size:15.5px;line-height:28px;color:var(--text)}
.small-btn{height:37px;line-height:37px;font-size:14px}

/* products */
.card{top:1575px;width:353px;height:491px;background:var(--white);box-shadow:0 2px 10px rgba(0,0,0,.18)}
.card .shot{position:absolute;left:96px;top:30px;width:160px;height:250px;background:linear-gradient(180deg,#9fd6ee,#2f8fcf 60%,#f0f4f7);border-radius:20px}
.card h4{position:absolute;left:0;top:308px;width:100%;text-align:center;font-size:22px;color:var(--ink);text-transform:uppercase}
.card p{position:absolute;left:30px;top:346px;width:293px;text-align:center;font-size:15.5px;line-height:21px;color:var(--ink)}
.card .price{position:absolute;left:0;top:392px;width:100%;text-align:center;font-size:20px;font-weight:700;color:var(--blue);text-decoration:line-through}
.card .btn{position:absolute;left:105px;top:424px;width:143px;height:31px;line-height:31px;font-size:14px;text-transform:none}

/* testimonials */
.band{left:0;top:2130px;width:1200px;height:379px;background:linear-gradient(180deg,#1f78cf,#1562b4)}
.band-title{left:0;top:2168px;width:1200px;text-align:center;font-size:27px;font-weight:700;color:var(--white)}
.quote{left:240px;top:2246px;width:740px;text-align:center;font-size:18.5px;line-height:26px;color:var(--white)}
.qmark{font-family:Georgia,serif;font-size:70px;color:var(--white);line-height:1}
.avatar{left:500px;top:2343px;width:76px;height:76px;border-radius:50%;background:linear-gradient(180deg,#c9b3a5,#6a4c3f);border:3px solid var(--white)}
.who{left:598px;top:2358px;color:var(--white)}
.who b{display:block;font-weight:400;font-size:19px}
.who span{font-size:14px}
.arrow{width:32px;height:32px;border:2px solid rgba(255,255,255,.7);border-radius:50%}
.dots{left:576px;top:2447px;display:flex;gap:8px}
.dots i{width:12px;height:12px;border-radius:50%;background:#0b3c74}
.dots i.on{background:var(--white)}

/* footer */
.footer{left:0;top:2509px;width:1200px;height:251px;background:var(--foot)}
.fcol h5{font-size:18px;color:var(--ink);text-transform:uppercase;margin-bottom:20px}
.fcol p{font-size:14px;line-height:23px;color:var(--muted)}
.field{width:228px;height:30px;background:#222;color:#ccc;font-size:12px;line-height:30px;padding-left:44px;position:relative;margin-top:18px}
.field svg{position:absolute;left:8px;top:6px}
.sub{width:92px;height:30px;line-height:30px;font-size:14px;margin-top:22px;text-transform:none}
.contact-row{display:flex;gap:12px;font-size:14px;color:var(--muted);line-height:19px;margin-bottom:16px}
.contact-row strong{color:var(--ink);font-weight:400}
.socials{display:flex;gap:20px;margin-top:6px}
.socials i{width:16px;height:16px;border-radius:50%;background:var(--blue)}
.bottom{left:0;top:2760px;width:1200px;height:52px;background:var(--blue-btn);color:var(--white);font-size:13px}
.bottom .links{position:absolute;left:47px;top:17px}
.bottom .copy{position:absolute;right:47px;top:17px}
</style>
</head>
<body>

<header>
  <div class="abs topbar"></div>
  <nav class="abs nav">
    <a class="active" style="width:88px">HOME</a>
    <a style="width:109px">ABOUT US</a>
    <a style="width:124px">PRODUCTS</a>
    <a style="width:105px">SERVICES</a>
    <a style="width:124px">RESOURCES</a>
    <a style="width:65px">FAQ</a>
    <a style="width:131px;border-right:1px solid rgba(255,255,255,.35)">CONTACT US</a>
  </nav>
  <div class="abs brand"><span class="brand-dot"></span><span class="brand-name">Velmora</span></div>
</header>

<section class="abs hero">
  <div class="abs hero-person" role="img" aria-label="Photo of a smiling woman holding a glass of water"></div>
  <div class="abs hero-product" role="img" aria-label="Photo of a countertop water purifier with a water splash"></div>
</section>
<h1 class="abs hero-title" style="font-weight:400">Keep your workforce healthy and productive with Velmora water purification systems</h1>
<a class="abs btn hero-btn">Read More</a>

<h2 class="abs section-title" style="top:697px">Know More Velmora</h2>
<svg class="abs ornament" style="top:732px" viewBox="0 0 140 20"><g stroke="#333" stroke-width="1.5"><line x1="0" y1="7" x2="62" y2="7"/><line x1="0" y1="12" x2="62" y2="12"/><line x1="78" y1="7" x2="140" y2="7"/><line x1="78" y1="12" x2="140" y2="12"/><line x1="66" y1="18" x2="72" y2="2"/><line x1="70" y1="18" x2="76" y2="2"/></g></svg>

<div class="abs cat" style="left:47px;width:352px">
  <h3>RO Water Purifiers</h3>
  <p>Lorem ipsum dolor sit amet, conseur adis cineliorbi tellus dui, vestibupor</p>
  <div class="shot" role="img" aria-label="Photo of a wall-mounted RO water purifier"></div>
</div>
<div class="abs cat" style="left:441px;width:326px">
  <h3>UV Water Purifiers</h3>
  <p>Lorem ipsum dolor sit amet, onseur adis cineliorbi tellus dui, vestibulum</p>
  <div class="shot" role="img" aria-label="Photo of a blue UV water purifier on a kitchen counter"></div>
</div>
<div class="abs cat" style="left:803px;width:352px">
  <h3>Gravity Water Purifiers</h3>
  <p>Lorem ipsum dolor sit amet, consect etur adis cineliorbi tellus dui, vestibul</p>
  <div class="shot" role="img" aria-label="Photo of a gravity water purifier"></div>
</div>

<h2 class="abs section-title" style="top:1179px">Welcome to Velmora</h2>
<svg class="abs ornament" style="top:1214px" viewBox="0 0 140 20"><g stroke="#333" stroke-width="1.5"><line x1="0" y1="7" x2="62" y2="7"/><line x1="0" y1="12" x2="62" y2="12"/><line x1="78" y1="7" x2="140" y2="7"/><line x1="78" y1="12" x2="140" y2="12"/><line x1="66" y1="18" x2="72" y2="2"/><line x1="70" y1="18" x2="76" y2="2"/></g></svg>
<p class="abs welcome-text">Lorem ipsum dolor sit amet, consectetur adipiscing elit. Cras elit magna, dignissim eu cursus iaculis, vestibulum ac mi. Quisque auctor metus quis nulla scelerisque, at condimentum sapien lacinia. Duis pellentesque cursus nibh non consequat. Vestibulum placerat lobortis diam. Maecenas placerat at nisl vel lacinia. Nullam rhoncus ipsum dolor, at iaculis augue maximus at. Etiam odio mauris, molestie quis accumsan auctor, dignissim sed tellus. Etiam iaculis nisi neque, quis aliquam nisi rutrum id. Integer tempor nulla mi, id sagittis dui eleifend ut. Maecenas at pretium sem. Suspendisse vulputate quam at urna porta varius. Proin id commodo erat.</p>
<a class="abs btn small-btn" style="left:549px;top:1397px;width:109px">Read More</a>

<h2 class="abs section-title" style="top:1482px">Products</h2>
<svg class="abs ornament" style="top:1518px" viewBox="0 0 140 20"><g stroke="#333" stroke-width="1.5"><line x1="0" y1="7" x2="62" y2="7"/><line x1="0" y1="12" x2="62" y2="12"/><line x1="78" y1="7" x2="140" y2="7"/><line x1="78" y1="12" x2="140" y2="12"/><line x1="66" y1="18" x2="72" y2="2"/><line x1="70" y1="18" x2="76" y2="2"/></g></svg>

<div class="abs card" style="left:47px">
  <div class="shot" role="img" aria-label="Product photo of a wall-mounted RO purifier"></div>
  <h4>Eco Chill RO</h4>
  <p>fermentum rutrum. Vivamus tortor ante, congue at sodales id auctor at auguno</p>
  <div class="price">$ 52,90</div>
  <a class="btn">Buy Now</a>
</div>
<div class="abs card" style="left:427px">
  <div class="shot" role="img" aria-label="Product photo of a blue UV purifier"></div>
  <h4>UV Grande</h4>
  <p>Lorem ipsum dolor sit amet onsectetur adipiscing elituspendisse ut arcu</p>
  <div class="price">$ 39,52,</div>
  <a class="btn">Buy Now</a>
</div>
<div class="abs card" style="left:806px">
  <div class="shot" role="img" aria-label="Product photo of a table top hot and cold purifier"></div>
  <h4>Icy Hot Table Top</h4>
  <p>Sed vitae vehicula nuullam vitae arcu non nisl varius ornare.sque eu iaculis tortor.</p>
  <div class="price">$ 549.00</div>
  <a class="btn">Buy Now</a>
</div>

<section class="abs band"></section>
<h2 class="abs band-title">TESTIMONILAS</h2>
<svg class="abs ornament" style="top:2205px" viewBox="0 0 140 20"><g stroke="#fff" stroke-width="1.5"><line x1="0" y1="7" x2="62" y2="7"/><line x1="0" y1="12" x2="62" y2="12"/><line x1="78" y1="7" x2="140" y2="7"/><line x1="78" y1="12" x2="140" y2="12"/><line x1="66" y1="18" x2="72" y2="2"/><line x1="70" y1="18" x2="76" y2="2"/></g></svg>
<span class="abs qmark" style="left:198px;top:2218px">&ldquo;</span>
<p class="abs quote">Lorem ipsum dolor sit amet, consectetur adipiscing elit. Nunc magna ex, lacinia vitae nunc eget, interdum mollis ex. Aliquam in lorem at eros lacinia vehicula ut at orci. Proin non quam sapien.Nulla in dictum augue. .Donec accumsan et nulla in interdum.</p>
<span class="abs qmark" style="left:906px;top:2295px">&rdquo;</span>
<div class="abs avatar" role="img" aria-label="Customer portrait"></div>
<div class="abs who"><b>Lorem isumn,</b><span>House wife City name</span></div>
<svg class="abs arrow" style="left:140px;top:2369px" viewBox="0 0 32 32"><path d="M18 10l-6 6 6 6" stroke="#fff" stroke-width="2" fill="none"/></svg>
<svg class="abs arrow" style="left:1036px;top:2369px" viewBox="0 0 32 32"><path d="M14 10l6 6-6 6" stroke="#fff" stroke-width="2" fill="none"/></svg>
<div class="abs dots"><i class="on"></i><i></i><i></i></div>

<footer>
  <div class="abs footer"></div>
  <div class="abs fcol" style="left:47px;top:2545px;width:380px">
    <h5>About Us</h5>
    <p>Lorem ipsum dolor sit amet, consectetur adipiscing elit. Suspendisse facilisis dictum metus eget elementum. Nunc lacinia euismod enim sed malesuada. In maximus ante vel sapien consectetur, at facilisis elit lacinia. Sed eleifend sit amet dui accumsan suscipit. Nullam metus purus, pulvinar sit amet egestas nec, elementum ac velit. Pellentesque</p>
  </div>
  <div class="abs fcol" style="left:542px;top:2545px;width:320px">
    <h5>Velmora Newsletters</h5>
    <p>Subscribe to keep up to date with Rivenmoor financial news, updates, roster additions and just plain old good stuff!!!!</p>
    <div class="field"><svg width="30" height="18" viewBox="0 0 30 18"><rect x="1" y="1" width="28" height="16" fill="none" stroke="#aaa"/><path d="M1 1l14 9 14-9" stroke="#aaa" fill="none"/></svg>your@email.com</div>
    <a class="btn sub">Subscribe</a>
  </div>
  <div class="abs fcol" style="left:922px;top:2545px;width:240px">
    <h5>Get in Touch</h5>
    <div class="contact-row">
      <svg width="16" height="22" viewBox="0 0 16 22"><path d="M8 1a7 7 0 0 1 7 7c0 5-7 13-7 13S1 13 1 8a7 7 0 0 1 7-7z" fill="#1565c0"/><circle cx="8" cy="8" r="2.5" fill="#fff"/></svg>
      <span><strong>Velmora Water Purification</strong><br>Lorem 9, Ispum doarl 8-12 amet Street Donec non leo NSW 123</span>
    </div>
    <div class="contact-row">
      <svg width="16" height="16" viewBox="0 0 16 16"><path d="M3 1l3 3-2 2c1 2 3 4 5 5l2-2 3 3-2 3C7 15 1 9 1 3z" fill="#1565c0"/></svg>
      <span>123 456 7890</span>
    </div>
    <div class="contact-row">
      <svg width="16" height="12" viewBox="0 0 16 12"><rect width="16" height="12" fill="#1565c0"/><path d="M0 0l8 6 8-6" stroke="#fff" fill="none"/></svg>
      <span>info@velmora-water.com</span>
    </div>
    <div class="socials"><i></i><i></i><i></i><i></i><i></i><i></i></div>
  </div>
  <div class="abs bottom">
    <div class="links">Home &nbsp;/&nbsp; About Us &nbsp;/&nbsp; Products &nbsp;/&nbsp; Services &nbsp;/&nbsp; Resources &nbsp;/&nbsp; Blog &nbsp;/&nbsp; Contact Us</div>
    <div class="copy">&copy; 2017 <b>Velmora Water Purification</b> All Rights Reserved.</div>
  </div>
</footer>

</body>
</html>
```